Medical centre needs a business card

We are a medcial centre in Australia, needing a new business card. Our demographic is low working class families. We are going to be renovating our premises to modernise the look and also had a new logo done a few months ago representing quality and community, and now need to update our cards. It needs to be doubled sided, with logo and contact details on the front, and appointment details on the back. . Needs to be modern and simple, easy to read. <br/><br/>Name: Fern Vale Medical Centre <br/>Address: 512 Kestrel Rd (Cnr Kestrel Rd & Lindon Park Rd),<br/>Corvane Court Shopping Centre, Paralowie, SA 5108<br/>Ph: 08 8361 4027<br/>Tag line: Where every visit counts for you<br/>Website: www.fernvalemedicalcentre.example.au<br/>Online bookings also available<br/><br/>(On the back, to have 3 lines of appointments that can be written in.<br/>Day, date, time)<br/><br/>Your next appointment is on<br/>Can try “M T W Th F Sa Su _________________ at ____________ am/pm” or other combinations <br/>Please advise as soon as possible if unable to attend<br/>Cancellation fees apply if less than 2 hrs notice<br/>Online appointments available (please highlight this option by either by position, colour or font)

Target Market(s)

Lower social economic working class, young families to seniors

Industry/Entity Type

Medical Centre

Contact Information for Business Card

Fern Vale Medical Centre
512 Kestrel Rd (Cnr Kestrel Rd & Lindon Park Drive)
Corvane Court Shopping Centre
Larkmoor SA 5190
Ph: 08 8361 4027
www.fernvalemedicalcentre.example.au
Tagline line: where every visit counts for you
Back side is for appointments
Your next appointment is with Dr ______________
Day/date/time (Please give 3 lines of appointments)
Please advise as soon as possible if unable to attend
Cancellation fees apply if less than 2 hours notice
Online appointments available
Book online easily and conveniently (please highlight online appointments)

Font styles to use
Serif
Sans Serif

Colors

Designer to choose colors to be used in the design.

Requirements
Must have
• Modern and simple
• Easy to ready
• Induces a wellbeing feeling
• Incorporate our logo colours and feel from logo
• Induces feeling of stability and security
Nice to have
• Attract attention
• Pleasant to look at
• Feeling of innovation
Should not have
• Loud clashing colours
• Overly luxurious feeling
• Overly artistic

```html
<!DOCTYPE html>
<html lang="en">
<head>
<meta charset="utf-8">
<title>Fern Vale Medical Centre – Business Card</title>
<link rel="stylesheet" href="https://fonts.googleapis.com/css2?family=Roboto:wght@400;500;700&display=swap">
<style>
  :root {
    --brand-blue: #1b7cc8;
    --brand-blue-light: #2a93d8;
    --paper: #ffffff;
    --backdrop: #e9ecef;
    --shadow: rgba(20, 40, 70, 0.18);
  }
  * { box-sizing: border-box; margin: 0; padding: 0; }
  html, body {
    width: 1200px; height: 900px; overflow: hidden;
    background: var(--backdrop);
    font-family: "Roboto", Arial, sans-serif;
  }
  .canvas { position: relative; width: 1200px; height: 900px; }
  .card {
    position: absolute; left: 250px;
    width: 700px; height: 400px;
    background: var(--paper);
    box-shadow: 0 6px 18px var(--shadow);
    overflow: hidden;
  }
  .card--front { top: 30px; }
  .card--back { top: 470px; }

  /* Front */
  .brand {
    position: absolute; top: 36px; left: 0; right: 0;
    display: flex; justify-content: center; align-items: center; gap: 14px;
  }
  .brand__dot {
    width: 34px; height: 34px; border-radius: 50%;
    background: var(--brand-blue);
  }
  .brand__name {
    color: var(--brand-blue); font-weight: 700; font-size: 30px; letter-spacing: 0.5px;
  }
  .contact {
    position: absolute; top: 98px; left: 0; right: 0;
    text-align: center; color: var(--brand-blue);
    font-size: 16px; line-height: 1.35;
  }
  .contact__icon {
    display: block; margin: 0 auto 3px; width: 20px; height: 20px;
  }
  .contact__group { margin-bottom: 7px; }
  .front-band {
    position: absolute; left: 0; right: 0; top: 322px; height: 52px;
    background: linear-gradient(90deg, var(--brand-blue), var(--brand-blue-light));
    display: flex; align-items: center; justify-content: center;
    color: var(--paper); font-size: 23px; font-weight: 500;
  }
  .front-edge {
    position: absolute; left: 0; right: 0; bottom: 0; height: 8px;
    background: var(--brand-blue);
  }

  /* Back */
  .back-top-line {
    position: absolute; left: 0; right: 0; top: 0; height: 10px;
    background: var(--brand-blue);
  }
  .back-title {
    position: absolute; top: 22px; left: 0; right: 0; text-align: center;
    color: var(--brand-blue); font-size: 34px; font-weight: 400;
  }
  .back-tagline {
    position: absolute; top: 66px; left: 0; right: 0; text-align: center;
    color: var(--brand-blue); font-size: 19px;
  }
  .appointment {
    position: absolute; left: 0; right: 0; top: 100px; height: 140px;
    background: linear-gradient(90deg, var(--brand-blue), var(--brand-blue-light));
    color: var(--paper); font-size: 21px; line-height: 1.55;
    padding: 16px 0 0 46px;
  }
  .notice {
    position: absolute; top: 254px; left: 46px; right: 20px;
    color: var(--brand-blue); font-size: 18px; line-height: 1.35;
  }
  .online-band {
    position: absolute; left: 0; right: 0; top: 318px; height: 52px;
    background: var(--brand-blue);
    color: var(--paper); font-size: 23px; font-weight: 500;
    display: flex; align-items: center; padding-left: 46px;
  }
</style>
</head>
<body>
<main class="canvas">

  <section class="card card--front" aria-label="Card front">
    <div class="brand">
      <span class="brand__dot"></span>
      <span class="brand__name">FERN VALE MEDICAL CENTRE</span>
    </div>
    <div class="contact">
      <div class="contact__group">
        <svg class="contact__icon" viewBox="0 0 20 20" aria-hidden="true">
          <circle cx="10" cy="10" r="10" fill="var(--brand-blue)"/>
          <path d="M10 4a4 4 0 0 0-4 4c0 3 4 8 4 8s4-5 4-8a4 4 0 0 0-4-4z" fill="#fff"/>
          <circle cx="10" cy="8" r="1.6" fill="var(--brand-blue)"/>
        </svg>
        512 Kestrel Rd (Cnr Kestrel Rd &amp; Lindon Park Drive)<br>
        Corvane Court Shopping Centre<br>
        Larkmoor SA 5190
      </div>
      <div class="contact__group">
        <svg class="contact__icon" viewBox="0 0 20 20" aria-hidden="true">
          <circle cx="10" cy="10" r="10" fill="var(--brand-blue)"/>
          <path d="M7 5l2 2-1 1.5a7 7 0 0 0 3.5 3.5L13 11l2 2-1.5 1.5C9.5 14 6 10.5 5.5 6.5z" fill="#fff"/>
        </svg>
        08 8361 4027
      </div>
      <div class="contact__group">
        <svg class="contact__icon" viewBox="0 0 20 20" aria-hidden="true">
          <circle cx="10" cy="10" r="10" fill="var(--brand-blue)"/>
          <circle cx="10" cy="10" r="5.5" fill="none" stroke="#fff" stroke-width="1.3"/>
          <path d="M4.5 10h11M10 4.5c-2.5 3-2.5 8 0 11M10 4.5c2.5 3 2.5 8 0 11" fill="none" stroke="#fff" stroke-width="1.1"/>
        </svg>
        www.fernvalemedicalcentre.example.au
      </div>
    </div>
    <div class="front-band">Where every visit counts for you</div>
    <div class="front-edge"></div>
  </section>

  <section class="card card--back" aria-label="Card back">
    <div class="back-top-line"></div>
    <h1 class="back-title">Fern Vale Medical Centre</h1>
    <p class="back-tagline">Where every visit counts for you</p>
    <div class="appointment">
      <p>Your next appointment is with Dr ____________________</p>
      <p>Day _○M _○T _○W _○Th _○F _○Sa _○Su</p>
      <p>Date __ /__ /____ &nbsp;Time ______ ○AM / ○PM</p>
    </div>
    <div class="notice">
      <p>Please advise as soon as possible if unable to attend</p>
      <p>(Cancellation fees apply if less than 2 hrs notice)</p>
    </div>
    <div class="online-band">Online appointments available</div>
  </section>

</main>
</body>
</html>
```